Design of labels for exciting new natural skincare products...natural deodorant

I need some labels designed for a range of natural skincare, initially a natural deodorant paste. i will be offering a range of fragrances so i want a basic idea that i can drop different colours / ingredients into easily.

Fragrances are:
1. Jasmine, Orange and Bergamot
2. Lavender & Bergamot
3. Peppermint & Tea tree
4. Unscented
5. Lime, Lemongrass & Ginger

I am a new startup and will be selling online and through a couple of specialty online stores. The final design should encompass our ethos which is clean and green, not fussy nor clinical but friendly and easily accessible. I like fresh, contemporary modern look referencing vintage aesthetics.

The idea is that these products are better for your body AND the environment, and we pledge to use no plastic to package or distribute our products. i like the use of contemporary pastels such as soft pinks, tans and green/blue/aquas, though am open to new ideas too. the logo (attached) appears in red but that should not necessarily be used. i also like black and white with touches of colour.

Target Market(s)

Eco aware, health concious consumers with a reasonable skincare budget.

Industry/Entity Type

Skin Care Product

Font styles to use
Serif
Sans Serif
Decorative

Colors
2eb6a2
b768aa
eea4c8
fabb94
85cae6
cfeae6
eaf2ce
000000
eaeaea

Requirements
Must have
• Labels are for a small glass jar - the dimensions are 2cm high only and wrapping around the jar - at least 10cm wide. i'm also going to be providing a smaller size so this needs to be able to scale down to 1.5cm high and 8cm wide.
• the logo (supplied)
• title: Natural Deodorant
• Subtitle: Orange, Jasmine & Bergamot
• 45g
• Ingredients: tapioca starch*, bicarbonate of soda, Coconut oil*, shea butter*, mango butter*, diatomaceous earth*, sweet almond oil*, vitamin e*, tea tree oil*, Sweet orange essential oil*, Jasmine essential oil*, Bergamot essential oil*.
• *Certified organic ingredient
• (DESIGNERS - PLEASE NOTE NOT ALL THE INGREDIENTS ARE ORGANIC, PLEASE LIST THEM WITH A STAR * IF I HAVE SUPPLIED IT, THEN *Certified organic ingredient BELOW IN SLIGHTLY SMALLER TEXT - THIS SERVES AS THE KEY FOR THE INGREDIENTS LIST)
• pebblewick.nz
• Massage a pea-sized amount onto clean, dry armpits for an odour-free day.
• If irritation develops discontinue use and contact Fern Hollow. (please italicise the company name)
Nice to have
• open to ideas - i am attaching some examples of designs i like, you'll notice i swing between plain black and white aesthetics and a more decorative look. In general i like the old "medicine bottle" look, with hand sketched illustrations. But i'm open to ideas!

```html
<!DOCTYPE html>
<html lang="en">
<head>
<meta charset="utf-8">
<title>Fern Hollow Natural Deodorant Label</title>
<link rel="stylesheet" href="https://fonts.googleapis.com/css2?family=Oswald:wght@300;400&family=Roboto+Condensed:wght@400&family=Dancing+Script:wght@600&family=Cabin:wght@400;600&display=swap">
<style>
  :root {
    --page: #f4f4f4;
    --plum: #9c3d8f;
    --plum-soft: #b768aa;
    --pink: #eea4c8;
    --teal: #2eb6a2;
    --cream: #ece7bf;
    --ink: #222222;
    --white: #ffffff;
    --badge: #3a3a3a;
  }
  html, body {
    margin: 0;
    width: 1134px;
    height: 1200px;
    overflow: hidden;
    background: var(--page);
  }
  .label {
    position: absolute;
    left: 27px;
    top: 492px;
    width: 1080px;
    height: 216px;
    box-shadow: 0 6px 18px rgba(0,0,0,0.12);
    overflow: hidden;
  }
  .label-front {
    position: absolute;
    left: 0; top: 0;
    width: 540px; height: 216px;
    background: linear-gradient(160deg, #b9dcea 0%, #dcecef 35%, #f3e2e6 65%, #f1bfcc 100%);
  }
  .front-shape {
    position: absolute;
    left: 0; top: 0;
  }
  .organic-badge {
    position: absolute;
    left: 158px; top: 40px;
    width: 54px; height: 54px;
    border-radius: 50%;
    background: var(--white);
    border: 4px solid var(--badge);
    box-sizing: border-box;
  }
  .brand-name {
    position: absolute;
    left: 222px; top: 44px;
    font-family: "Oswald", sans-serif;
    font-weight: 400;
    font-size: 30px;
    line-height: 1;
    color: var(--cream);
  }
  .product-title {
    position: absolute;
    left: 114px; width: 307px;
    top: 99px;
    text-align: center;
    font-family: "Oswald", sans-serif;
    font-weight: 300;
    font-size: 29px;
    line-height: 1;
    color: var(--white);
  }
  .scent-ribbon {
    position: absolute;
    left: 165px; top: 134px;
    width: 209px; height: 28px;
    background: var(--teal);
    clip-path: polygon(0 0, 100% 0, 97% 50%, 100% 100%, 0 100%, 3% 50%);
    color: var(--white);
    font-family: "Cabin", sans-serif;
    font-size: 14px;
    line-height: 28px;
    text-align: center;
  }
  .net-weight {
    position: absolute;
    left: 114px; width: 307px;
    top: 170px;
    text-align: center;
    font-family: "Cabin", sans-serif;
    font-weight: 600;
    font-size: 13px;
    color: var(--white);
  }
  .label-back {
    position: absolute;
    left: 540px; top: 0;
    width: 540px; height: 216px;
    background: radial-gradient(ellipse at 50% 40%, #ffffff 0%, #f6f6f6 100%);
  }
  .ingredients-heading {
    position: absolute;
    left: 0; width: 564px;
    top: 16px;
    text-align: center;
    font-family: "Dancing Script", cursive;
    font-weight: 600;
    font-size: 28px;
    line-height: 1;
    color: var(--plum-soft);
  }
  .ingredients-list {
    position: absolute;
    left: 40px; width: 484px;
    top: 55px;
    margin: 0;
    text-align: center;
    font-family: "Roboto Condensed", sans-serif;
    font-size: 14px;
    line-height: 18.5px;
    color: var(--ink);
  }
  .divider {
    position: absolute;
    left: 57px; width: 434px;
    top: 135px;
    height: 1px;
    background: var(--plum-soft);
  }
  .usage-note {
    position: absolute;
    left: 57px; top: 144px;
    margin: 0;
    font-family: "Roboto Condensed", sans-serif;
    font-size: 14px;
    line-height: 16px;
    color: var(--teal);
  }
  .mark {
    position: absolute;
    top: 145px;
    width: 30px; height: 30px;
    background: var(--ink);
  }
  .mark-cruelty { left: 366px; border-radius: 4px; background: #6a6a6a; }
  .mark-origin { left: 408px; border-radius: 4px; }
  .mark-recycle { left: 458px; border-radius: 50%; }
  .web-pill {
    position: absolute;
    left: 193px; top: 187px;
    width: 252px; height: 34px;
    border-radius: 12px 12px 0 0;
    background: var(--plum-soft);
    color: var(--white);
    font-family: "Oswald", sans-serif;
    font-weight: 400;
    font-size: 15px;
    letter-spacing: 1.5px;
    line-height: 29px;
    text-align: center;
  }
</style>
</head>
<body>
  <div class="label">
    <section class="label-front">
      <svg class="front-shape" width="540" height="216" viewBox="0 0 540 216">
        <polygon points="165,-4 368,-4 421,108 368,220 165,220 114,108" fill="var(--plum)" stroke="var(--pink)" stroke-width="5"/>
      </svg>
      <div class="organic-badge" role="img" aria-label="Organic ingredients badge"></div>
      <div class="brand-name">Fern Hollow</div>
      <div class="product-title">NATURAL DEODORANT</div>
      <div class="scent-ribbon">Orange, Jasmine &amp; Bergamot</div>
      <div class="net-weight">45G</div>
    </section>
    <section class="label-back">
      <div class="ingredients-heading">Ingredients</div>
      <p class="ingredients-list">Coconut oil*, tapioca starch*, bicarbonate of soda, shea butter*, mango<br>butter*, diatomaceous earth*, sweet almond oil*, vitamin e*, tea tree oil*,<br>Sweet orange essential oil*, Jasmine essential oil*,<br>Bergamot essential oil*.</p>
      <div class="divider"></div>
      <p class="usage-note">Massage a pea-sized amount onto clean,<br>dry armpits for an odour-free day.</p>
      <div class="mark mark-cruelty" role="img" aria-label="Cruelty free badge"></div>
      <div class="mark mark-origin" role="img" aria-label="Country of origin badge"></div>
      <div class="mark mark-recycle" role="img" aria-label="Recyclable badge"></div>
      <div class="web-pill">WWW.PEBBLEWICK.NZ</div>
    </section>
  </div>
</body>
</html>
```